Harbor Sushi & Steak Dinner Menu

I'm looking for a MENU design with a particular feel. I want to have a base template made that I can then use for future alterations to the menu; ie I can go in and change out different entrees as the menu changes but the template will remain the same. (Ideally it would be in an Apple Pages format.). Also ideally - dinner menu will occupy 2 pages 8.5 x 11. The restaurant's name is Harbor. It is a MODERN steak house that will also feature Sushi, a Raw Bar, Exquisite Cocktails and a sophisticated nightlife crowd. I have attached our LOGO, a secondary logo that we will be featuring throughout the project including on the menu cover (the gold U). Finally - I have attached the content that we would like to see. AGAIN - I REITERATE: High end dining and lounge atmosphere. A couple of restaurants / menus that I love are Morvendel in NYC and Pellucid Steakhouse in Long Island NY. Please do not duplicate - just trying to offer some suggestions.

Requirements
Must have
• A sophisticated and elegant feel without being stuffy or old.

```html
<!DOCTYPE html>
<html lang="en">
<head>
<meta charset="utf-8">
<title>Harbor Sushi &amp; Steak — Sushi Menu</title>
<link rel="stylesheet" href="https://fonts.googleapis.com/css2?family=Source+Sans+3:wght@400;600;700&display=swap">
<style>
  :root {
    --backdrop: #e8e3da;
    --menu-black: #0c0c0c;
    --gold: #d6bf7d;
    --gold-box: #d3bb78;
    --red: #c62b3e;
    --ink-light: #f2f0ea;
    --ink-dark: #141414;
  }
  * { margin: 0; padding: 0; box-sizing: border-box; }
  html, body {
    width: 1200px; height: 800px; overflow: hidden;
    background: var(--backdrop);
    font-family: "Source Sans 3", "Helvetica Neue", Arial, sans-serif;
  }
  .menu-card {
    position: absolute; left: 384px; top: 76px;
    width: 432px; height: 648px;
    background: var(--menu-black);
    color: var(--ink-light);
  }
  .brand {
    position: absolute; top: 34px; left: 0; width: 100%;
    display: flex; justify-content: center; align-items: center; gap: 10px;
  }
  .brand-dot { width: 12px; height: 12px; border-radius: 50%; background: var(--red); }
  .brand-name {
    font-size: 36px; font-weight: 600; letter-spacing: 5px;
    color: var(--gold); line-height: 1;
  }
  .section-title {
    position: absolute; top: 128px; left: 24px; width: 384px;
    display: flex; align-items: center; justify-content: space-between;
  }
  .section-title .rule { width: 92px; height: 1px; background: var(--gold); }
  .section-title h1 {
    font-size: 19px; font-weight: 700; color: var(--gold); letter-spacing: 0.5px;
  }
  .nigiri-list {
    position: absolute; top: 161px; list-style: none;
    font-size: 9.5px; line-height: 16px; text-align: center;
  }
  .nigiri-list b { font-weight: 700; }
  .nigiri-left { left: 40px; width: 206px; }
  .nigiri-right { left: 234px; width: 144px; }
  .platters {
    position: absolute; top: 256px; left: 25px; width: 377px; height: 76px;
    background: var(--gold-box); color: var(--ink-dark);
    border: 1.5px dotted #3a3222; outline: 2px solid var(--gold-box);
    padding: 8px 10px 0;
  }
  .platters h2 { font-size: 13px; font-weight: 700; text-align: center; margin-bottom: 4px; }
  .platters p { font-size: 9px; line-height: 16px; }
  .platters b { font-weight: 700; }
  .roll-column { position: absolute; top: 344px; width: 180px; }
  .roll-classic { left: 32px; }
  .roll-special { left: 228px; }
  .roll-column h2 {
    font-size: 13px; font-weight: 700; color: var(--red); margin-bottom: 10px; letter-spacing: 0.3px;
  }
  .roll-column p { font-size: 9.5px; line-height: 16px; }
  .roll-column b { font-weight: 700; }
</style>
</head>
<body>
  <main class="menu-card">
    <header class="brand">
      <span class="brand-dot"></span>
      <span class="brand-name">HARBOR</span>
    </header>

    <div class="section-title">
      <span class="rule"></span>
      <h1>SUSHI / SASHIMI</h1>
      <span class="rule"></span>
    </div>

    <ul class="nigiri-list nigiri-left">
      <li><b>TORO</b> - blue fin tuna belly (gf)</li>
      <li><b>EBI</b> - cooked shrimp (gf)</li>
      <li><b>HAMACHI</b> - yellowtail (gf)</li>
      <li><b>UNI</b> - sea urchin (gf)</li>
      <li><b>HIRAME</b> - fluke (gf)</li>
    </ul>
    <ul class="nigiri-list nigiri-right">
      <li><b>UNAGI</b> - fresh water eel (gf)</li>
      <li><b>SAKE</b> - salmon (gf)</li>
      <li><b>MADAI</b> - ed snapper (gf)</li>
      <li><b>MAGURO</b> - tuna (gf)</li>
    </ul>

    <section class="platters">
      <h2>SUSHI PLATTERS</h2>
      <p><b>Small:</b> Five Pieces assorted sushi, nine pieces sashimi, spicy tuna roll (gf)</p>
      <p><b>Large:</b> Eight Pieces assorted sushi, eighteen pieces of sashimi, alaskan roll, rainbow roll (gf)</p>
    </section>

    <section class="roll-column roll-classic">
      <h2>CLASSIC ROLLS</h2>
      <p><b>Yellowtail;</b> inside out roll with scallions (gf)</p>
      <p><b>Spicy Tuna or Salmon or Yellowtail;</b> spicy mayo</p>
      <p><b>California:</b> crab meat, cucumber and avocado (gf)</p>
      <p><b>Vegetable:</b> avocado, cucumber, asparagus and pickled reddish (gf)</p>
      <p><b>Spider:</b> soft shell crab and avocado with eel sauce</p>
      <p><b>Shrimp Tempura:</b> deep fried tempura shrimp and eel sauce Alaskan; salmon and avocado (gf)</p>
    </section>

    <section class="roll-column roll-special">
      <h2>SPECIAL ROLLS</h2>
      <p><b>The Harbor:</b> tuna, salmon, yellowtail, avocado, spicy mayo, soy bean paper</p>
      <p><b>King Crab Rainbow:</b> king crab, avocado, cucumbers, assorted fish on top</p>
      <p><b>Empress:</b> Shrimp tempura, spicy tuna on top, eel sauce, spicy mayo</p>
      <p><b>Spicy Girl:</b> Spicy crunchy crab meat, cucumber, shrimp on top</p>
      <p><b>Dragon:</b> Eel, cucumber, avocado, and tobiko on top, eel sauce</p>
      <p><b>Yummy:</b> spicy crunchy salmon, avocado, mango and salmon on top</p>
      <p><b>No. 9:</b> Shrimp Tempura, avocado, kani, spicy mayo, tobiko</p>
      <p><b>Sunrise Roll:</b> spicy crunchy tuna and avocado, spicy crunchy salmon on top</p>
    </section>
  </main>
</body>
</html>
```